Cage Free Dog Resort under new ownership needs New Logo & Website Redesign

We need a logo design and updated website for our new business. We offer cage free boarding services for dogs where they are free to run & play outside during the day. The current website has lots of brown & orange & we would like the new website to be more visually attractive utilizing more pictures of dogs playing and having fun.

Target Market(s)

Dog lovers with disposable income to afford special care for their pets - looking for a place for their dogs to be pampered while they are away from home. Primarily dogs, but we will also board cats and other pets too.

Industry/Entity Type

Pet Care

Logo Text

Willow Bend Pet Lodge

Coding

Coded - Design and coding required

Number of Pages Required

5+ page

Font styles to use
Sans Serif

Colors
0692cd
fbee3d
f04a50

Requirements
Must have
• Current website is www.willowbendpetlodge.example
• I would like for someone to click on our website & have the "oh that is so cute/awesome/what a great looking place" reaction!
• Link to pages with forms
• Stock photos of different breeds of dogs having fun playing out doors
• Gallery Photo page (where I can go in and update with new pictures)
Nice to have
• Tag line something like - "Your best friend's home away from home!"
• Some cartoon type dogs/cats
Should not have
• Wasn't sure about font below - so whichever font is easiest to read and still looks professional

```html
<!DOCTYPE html>
<html lang="en">
<head>
<meta charset="utf-8">
<title>Willow Bend Pet Lodge &amp; Doggie Daycare</title>
<link href="https://fonts.googleapis.com/css2?family=Poppins:ital,wght@0,400;0,500;0,600;0,700;1,400&display=swap" rel="stylesheet">
<style>
:root{
  --blue:#1479c4;
  --blue-bright:#0692cd;
  --yellow:#f7ea36;
  --yellow-pale:#fbf3a0;
  --red:#f0081f;
  --red-soft:#f04a50;
  --ink:#1b1b1b;
  --grey-card:#ededed;
  --white:#ffffff;
}
*{box-sizing:border-box;margin:0;padding:0}
html,body{width:1200px;height:3077px;overflow:hidden}
body{position:relative;font-family:'Poppins',Arial,sans-serif;color:var(--ink);background:var(--white)}
.abs{position:absolute}
.backdrop{position:absolute;left:0;top:0;width:1200px;height:3077px}

/* header */
.site-header{left:0;top:0;width:1200px;height:94px;background:var(--white)}
.brand{left:62px;top:22px;display:flex;align-items:center;gap:14px}
.brand-dot{width:58px;height:58px;border-radius:50%;background:var(--red-soft)}
.brand-name{font-weight:600;font-size:25px;line-height:30px;color:var(--red)}
.call-pill{left:925px;top:18px;width:216px;height:40px;border-radius:20px;background:var(--yellow);display:flex;align-items:center;justify-content:center;gap:10px;font-size:15px;font-weight:500}
.main-nav{left:537px;top:70px;width:603px;height:40px;background:var(--blue);border-radius:0 20px 20px 0;display:flex;align-items:center;font-size:14px;color:var(--white)}
.main-nav a{color:inherit;text-decoration:none;padding:0 16px;height:40px;display:flex;align-items:center}
.main-nav a.active{background:var(--red);padding:0 22px 0 34px;clip-path:polygon(14px 0,100% 0,100% 100%,0 100%)}

/* hero */
.hero-photo{left:0;top:94px;width:1200px;height:620px;background:linear-gradient(180deg,#8fae6a 0%,#5c8a3a 45%,#3f6e25 100%)}
.hero-dogs{left:330px;top:180px;width:480px;height:440px;border-radius:40%;background:radial-gradient(ellipse at center,#8a4a26 0%,rgba(120,70,40,.6) 45%,rgba(90,120,60,0) 72%)}
.tagline{left:0;top:340px;width:1200px;text-align:center;color:var(--white);font-weight:600;font-size:30px;text-shadow:0 2px 6px rgba(0,0,0,.35)}
.btn{display:inline-flex;align-items:center;justify-content:center;width:140px;height:42px;border-radius:21px;background:var(--yellow);font-weight:600;font-size:16px;color:var(--ink);text-decoration:none}
.hero-btn{left:530px;top:402px}
.quote-box{left:234px;top:470px;width:732px;height:136px;border-radius:18px;background:rgba(30,30,30,.72);color:var(--white)}
.quote-avatar{left:44px;top:18px;width:100px;height:100px;border-radius:50%;background:linear-gradient(160deg,#d9b08c,#8a5a3a)}
.quote-text{left:174px;top:22px;width:520px;font-size:16px;line-height:27px}
.scroll-btn{left:575px;top:640px;width:50px;height:50px;border-radius:50%;background:var(--white);box-shadow:0 2px 6px rgba(0,0,0,.2);display:flex;align-items:center;justify-content:center}

/* welcome */
.deco{background:rgba(255,255,255,.55);border-radius:50%}
.welcome-title{left:0;top:790px;width:1200px;text-align:center;color:var(--white);font-size:44px;font-weight:400}
.welcome-title strong{font-weight:700}
.welcome-text{left:140px;top:852px;width:920px;text-align:center;color:var(--white);font-size:16.5px;line-height:22px}
.welcome-btn{left:530px;top:1004px}

/* gallery */
.section-title{left:0;width:1200px;text-align:center;font-weight:700;font-size:42px}
.gallery-title{top:1196px;color:var(--white)}
.gallery-grid{left:62px;top:1286px;width:1078px;height:720px;display:grid;grid-template-columns:repeat(3,1fr);grid-template-rows:repeat(2,1fr)}
.gallery-grid div{width:100%;height:100%}

/* testimonials */
.testi-title{top:2176px;color:var(--blue)}
.testi-card{top:2303px;width:496px;height:196px;background:var(--grey-card);text-align:center}
.testi-card .name{margin-top:32px;font-style:italic;font-size:25px}
.testi-card .body{margin:10px auto 0;width:400px;font-style:italic;font-size:15px;line-height:21px}
.testi-avatar{width:110px;height:110px;border-radius:50%}

/* footer */
.footer-mark{left:570px;top:2672px;width:60px;height:60px;border-radius:50%;background:var(--red)}
.footer-name{left:0;top:2740px;width:1200px;text-align:center;font-weight:600;font-size:24px;line-height:30px;color:var(--red)}
.socials{left:510px;top:2812px;display:flex;gap:10px}
.socials span{width:32px;height:32px;border-radius:50%;background:#d9d9d9}
.contact{left:0;top:2858px;width:1200px;text-align:center;color:var(--red);font-weight:600;font-size:25px;line-height:31px}
.footer-nav{left:0;top:2972px;width:1200px;display:flex;justify-content:center;gap:42px;font-size:13px}
.footer-nav a{color:var(--ink);text-decoration:none}
.copyright{left:0;top:3012px;width:1200px;text-align:center;font-size:11px;color:#444}
</style>
</head>
<body>

<div class="abs hero-photo" role="img" aria-label="Photo of two small dogs running across a sunny lawn, one carrying a red ball"></div>
<div class="abs hero-dogs" aria-hidden="true"></div>

<svg class="backdrop" viewBox="0 0 1200 3077" aria-hidden="true">
  <!-- blue welcome band -->
  <path d="M0 636 L1200 708 L1200 1130 L0 1130 Z" fill="var(--blue)"/>
  <!-- red gallery band -->
  <path d="M0 1132 C120 1090 260 1098 420 1090 C560 1082 720 1030 860 1050 C1000 1070 1090 1120 1200 1112 L1200 2120 L0 2120 Z" fill="var(--red-soft)"/>
  <path d="M0 1142 C140 1104 280 1112 440 1104 C580 1096 740 1046 880 1064 C1010 1082 1100 1130 1200 1124 L1200 2120 L0 2120 Z" fill="var(--red)"/>
  <!-- yellow testimonials band -->
  <path d="M0 2120 C80 2060 160 2030 260 2050 C360 2070 420 2100 560 2080 C700 2060 780 2090 900 2100 C1020 2110 1120 2080 1200 2060 L1200 2700 L0 2700 Z" fill="var(--yellow)"/>
  <!-- footer wave -->
  <path d="M0 2650 C200 2640 380 2600 560 2555 C700 2522 860 2560 1000 2610 C1080 2636 1150 2640 1200 2630 L1200 3077 L0 3077 Z" fill="var(--yellow-pale)"/>
  <path d="M0 2700 C200 2690 380 2650 560 2602 C700 2568 860 2600 1000 2650 C1080 2676 1150 2680 1200 2670 L1200 3077 L0 3077 Z" fill="var(--white)"/>
</svg>

<header class="abs site-header">
  <div class="abs brand">
    <span class="brand-dot"></span>
    <span class="brand-name">Willow Bend Pet Lodge &amp;<br>Doggie Daycare</span>
  </div>
  <div class="abs call-pill">
    <svg width="14" height="14" viewBox="0 0 24 24" aria-hidden="true"><path d="M6.6 10.8a15.1 15.1 0 0 0 6.6 6.6l2.2-2.2a1 1 0 0 1 1-.25 11.4 11.4 0 0 0 3.6.57 1 1 0 0 1 1 1V20a1 1 0 0 1-1 1A17 17 0 0 1 3 4a1 1 0 0 1 1-1h3.5a1 1 0 0 1 1 1 11.4 11.4 0 0 0 .57 3.6 1 1 0 0 1-.25 1z" fill="#1b1b1b"/></svg>
    Call Us : 555/014-2290
  </div>
</header>
<nav class="abs main-nav">
  <a class="active" href="#">Home</a>
  <a href="#">About Us</a>
  <a href="#">Rates and Hours</a>
  <a href="#">Accommodations</a>
  <a href="#">Contact Us</a>
</nav>

<h1 class="abs tagline">Your best friend's home away from home!</h1>
<a class="abs btn hero-btn" href="#">Learn More</a>

<div class="abs quote-box">
  <div class="abs quote-avatar" role="img" aria-label="Portrait photo of a smiling client"></div>
  <p class="abs quote-text">We do daycare as well as overnight and our guests love it! They drag their owners in the gate.<br>"Miss Dana"</p>
</div>

<div class="abs scroll-btn">
  <svg width="16" height="16" viewBox="0 0 16 16" aria-hidden="true"><path d="M3 6l5 5 5-5" fill="none" stroke="#1b1b1b" stroke-width="2"/></svg>
</div>

<div class="abs" style="left:564px;top:706px;width:72px;height:66px;border-radius:50%;background:#c98a4e" role="img" aria-label="Cartoon puppy face illustration"></div>
<div class="abs deco" style="left:168px;top:724px;width:86px;height:56px" role="img" aria-label="Cartoon moon and cloud illustration"></div>
<div class="abs deco" style="left:958px;top:730px;width:118px;height:70px" role="img" aria-label="Cartoon cloud illustration"></div>
<div class="abs deco" style="left:122px;top:992px;width:50px;height:26px;opacity:.5" role="img" aria-label="Small cloud illustration"></div>
<div class="abs deco" style="left:740px;top:990px;width:50px;height:26px;opacity:.5" role="img" aria-label="Small cloud illustration"></div>
<div class="abs" style="left:74px;top:1060px;width:66px;height:70px;border-radius:30%;background:#e2a23a" role="img" aria-label="Cartoon sitting dog illustration"></div>

<h2 class="abs welcome-title">Welcome To <strong>Willow Bend Pet Lodge</strong></h2>
<p class="abs welcome-text">Willow Bend Pet Lodge in Maple Creek offers socialized no cage dog boarding in a family environment. Our guests enjoy free run of spacious yards during the day and comfy bedrooms. great alternative to dog boarding<br><br>animal care in Maple Creek or anywhere else!</p>
<a class="abs btn welcome-btn" href="#">Learn More</a>

<div class="abs" style="left:308px;top:1152px;width:56px;height:56px;border-radius:50%;background:var(--red-soft)" role="img" aria-label="Star burst ornament"></div>
<div class="abs" style="left:924px;top:1244px;width:50px;height:50px;border-radius:50%;background:var(--red-soft)" role="img" aria-label="Star burst ornament"></div>

<h2 class="abs section-title gallery-title">Gallery</h2>
<div class="abs gallery-grid">
  <div role="img" aria-label="Photo of a beagle and a small white dog resting on a playground" style="background:linear-gradient(160deg,#e8a64a,#9c6a3a 60%,#c7c2b8)"></div>
  <div role="img" aria-label="Photo of two dogs tugging a green flying disc" style="background:linear-gradient(160deg,#4d8a3a,#2a2a2a 55%,#7a4a2a)"></div>
  <div role="img" aria-label="Photo of a white puppy and two kittens in the grass" style="background:linear-gradient(160deg,#6a9a3a,#e4e2da 55%,#8a7a5a)"></div>
  <div role="img" aria-label="Photo of a beagle puppy running with a red ball" style="background:linear-gradient(160deg,#4a6a2a,#c99a6a 55%,#5c8a2c)"></div>
  <div role="img" aria-label="Photo of a black and white border collie running toward the camera" style="background:linear-gradient(160deg,#a89a2a,#2a2a2a 55%,#6a8a2a)"></div>
  <div role="img" aria-label="Photo of two small brown dogs sitting in a sunny meadow" style="background:linear-gradient(160deg,#b89a3a,#7a4a2a 55%,#8aa23a)"></div>
</div>

<div class="abs" style="left:364px;top:2002px;width:40px;height:40px;border-radius:50%;background:var(--red-soft)" role="img" aria-label="Star burst ornament"></div>
<div class="abs" style="left:966px;top:2074px;width:52px;height:52px;border-radius:50%;background:var(--red-soft)" role="img" aria-label="Star burst ornament"></div>
<div class="abs" style="left:140px;top:2140px;width:80px;height:66px;border-radius:40%;background:#e9c92f" role="img" aria-label="Paw print pattern"></div>
<div class="abs" style="left:1042px;top:2206px;width:80px;height:66px;border-radius:40%;background:#e9c92f" role="img" aria-label="Paw print pattern"></div>
<div class="abs" style="left:592px;top:2460px;width:80px;height:66px;border-radius:40%;background:#e9c92f" role="img" aria-label="Paw print pattern"></div>
<div class="abs" style="left:572px;top:2118px;width:56px;height:54px;border-radius:50%;background:#e9a23a" role="img" aria-label="Cartoon cat face illustration"></div>

<h2 class="abs section-title testi-title">Testimonials</h2>
<article class="abs testi-card" style="left:76px">
  <p class="name">Marta</p>
  <p class="body">" Phasellus vulputate nulla. Morbi at dui hac amet vulputate vestibulum class sapien integer consectetuer phasellus ac congue class. Nunc dictumst metus vulputate urna vel."</p>
</article>
<div class="abs testi-avatar" style="left:101px;top:2236px;background:#2a9be0" role="img" aria-label="Illustration of a woman holding a small dog"></div>
<article class="abs testi-card" style="left:626px">
  <p class="name">Owen</p>
  <p class="body">" Phasellus vulputate nulla. Morbi at dui hac amet vulputate vestibulum class sapien integer consectetuer phasellus ac congue class. Nunc dictumst metus vulputate urna vel."</p>
</article>
<div class="abs testi-avatar" style="left:644px;top:2236px;background:#c42a1e" role="img" aria-label="Illustration of a person hugging a dog"></div>

<footer>
  <div class="abs footer-mark"></div>
  <p class="abs footer-name">Willow Bend Pet Lodge &amp;<br>Doggie Daycare</p>
  <div class="abs socials" aria-label="Social links"><span></span><span></span><span></span><span></span><span></span></div>
  <p class="abs contact">Contact Us: 555/014-2290<br>or<br>willowbendpetlodge@mail.example</p>
  <nav class="abs footer-nav">
    <a href="#">Home</a><a href="#">About Us</a><a href="#">Rates and Hours</a><a href="#">Accommodations</a><a href="#">Contact US</a>
  </nav>
  <p class="abs copyright">© Copyright 2018 | www.willowbendpetlodge.example</p>
</footer>

</body>
</html>
```